MGC Business Card Design

I am a wedding and event Planner. I have just completed a name change from Soirees by Lucette to The Gathering Corner and I just received my new logo and need new business cards to match my new brand. Elegant, chic and upscale yet simple. I am drafting a new website on my old (for drafting purposes). You can take a look and it will give you an idea of the direction of my brand. (www.soireesbylucette.example). I would like gray and white colors and it can be a shaded mixture of grays. I am open in regard to placement of the information

Target Market(s)

Brides, Corporate Companies, Families etc.

Industry/Entity Type

Wedding

Contact Information for Business Card

The Gathering Corner
www.mygatheringcorner.example
Event Planning and Design Firm
Lucette M. Harlow, Owner/CEO
Certified Event & Wedding Planner
T: (555) 214-7390 | F: (555) 307-4128
E: wegather@mygatheringcorner.example
(please put T, E & F letters in a script font)

Love to Plan. Plan to Live. Live to Love. (lh)

(social icons instead of text)
twitter: @gatheringcorner1
facebook: @thegatheringcorner
Pinterest: @gatheringcorner
instagram: @thegatheringcorner1

Can we put a barcode leading to my website

```html
<!DOCTYPE html>
<html lang="en">
<head>
<meta charset="utf-8">
<title>The Gathering Corner – Business Card</title>
<link rel="stylesheet" href="https://fonts.googleapis.com/css2?family=Share+Tech+Mono&display=swap">
<style>
  :root {
    --card-bg: #ffffff;
    --ink: #4a5558;
    --chip-light: #8f999b;
    --chip-mid: #737c7e;
    --chip-dark: #535b5d;
  }
  html, body {
    margin: 0;
    padding: 0;
    width: 1200px;
    height: 702px;
    overflow: hidden;
    background: var(--card-bg);
  }
  .card {
    position: relative;
    width: 1200px;
    height: 702px;
    background: var(--card-bg);
    font-family: "Share Tech Mono", monospace;
    color: var(--ink);
    font-size: 30px;
    letter-spacing: 1.5px;
  }
  .card-details {
    position: absolute;
    top: 221px;
    left: 0;
    width: 1200px;
    margin: 0;
    padding: 0;
    list-style: none;
    text-align: center;
  }
  .card-details li {
    height: 37px;
    line-height: 37px;
    white-space: nowrap;
  }
  .social-list {
    position: absolute;
    top: 517px;
    left: 431px;
    margin: 0;
    padding: 0;
    list-style: none;
  }
  .social-item {
    display: flex;
    align-items: center;
    height: 37px;
    line-height: 37px;
    white-space: nowrap;
  }
  .social-chip {
    width: 31px;
    height: 31px;
    margin-right: 10px;
    border-radius: 2px;
    flex: none;
  }
  .chip-light { background: var(--chip-light); }
  .chip-mid { background: var(--chip-mid); }
  .chip-dark { background: var(--chip-dark); }
</style>
</head>
<body>
  <main class="card">
    <ul class="card-details">
      <li class="business-name">The Gathering Corner</li>
      <li class="website">www.mygatheringcorner.example</li>
      <li class="tagline">Event Planning and Design Firm</li>
      <li class="owner">Lucette M. Harlow, Owner/CEO</li>
      <li class="credential">Certified Event &amp; Wedding Planner</li>
      <li class="phone">T: (555) 214-7390</li>
      <li class="fax">F:(555) 307-4128</li>
      <li class="email">E: wegather@mygatheringcorner.example</li>
    </ul>
    <ul class="social-list">
      <li class="social-item"><span class="social-chip chip-light"></span>@gatheringcorner1</li>
      <li class="social-item"><span class="social-chip chip-dark"></span>@thegatheringcorner</li>
      <li class="social-item"><span class="social-chip chip-mid"></span>@gatheringcorner</li>
      <li class="social-item"><span class="social-chip chip-dark"></span>@thegatheringcorner1</li>
    </ul>
  </main>
</body>
</html>
```